Business Card Design Project

A business card for a new company in Ontario Canada called Build for Growth. It is a consulting company which uses Brixo as the medium for facilitation.

The target market is for senior leaders in healthcare and social services.

Industry/Entity Type

Healthcare

Requirements
Must have
• The name Build For Growth
Dana Montreuil RRT, B Ed (AD ed).
Tacticraft Facililitator (R)

Tag Line
Engaging Transforming and Innovative
The attached logo

danamontreuil@examplemail.com
416-555-0147
Should not have
• Lime green
Times New Roman or Arial font
Do not include Brixo bricks on the card.

```html
<!DOCTYPE html>
<html lang="en">
<head>
<meta charset="utf-8">
<title>Build For Growth – Business Card</title>
<link rel="stylesheet" href="https://fonts.googleapis.com/css2?family=Anton&family=Archivo+Black&family=Open+Sans:wght@300;400&display=swap">
<style>
  :root {
    --brand-blue: #5b8fc7;
    --ink: #111111;
    --logo-purple: #5f2a8c;
    --paper: #ffffff;
  }
  html, body {
    margin: 0;
    padding: 0;
    width: 1200px;
    height: 677px;
    overflow: hidden;
    background: var(--paper);
  }
  .card {
    position: relative;
    width: 1200px;
    height: 677px;
    background: var(--paper);
    overflow: hidden;
  }
  .side-band {
    position: absolute;
    left: 0;
    top: 0;
    width: 111px;
    height: 677px;
    background: var(--brand-blue);
  }
  .company-name {
    position: absolute;
    left: 198px;
    top: 60px;
    margin: 0;
    font-family: "Anton", sans-serif;
    font-weight: 400;
    font-size: 122px;
    line-height: 1;
    letter-spacing: 4px;
    color: var(--brand-blue);
    white-space: nowrap;
  }
  .person-name {
    position: absolute;
    left: 197px;
    top: 218px;
    margin: 0;
    font-family: "Archivo Black", sans-serif;
    font-size: 40px;
    line-height: 1;
    color: var(--ink);
    white-space: nowrap;
  }
  .person-title {
    position: absolute;
    left: 197px;
    top: 266px;
    margin: 0;
    font-family: "Archivo Black", sans-serif;
    font-size: 24px;
    line-height: 1;
    color: var(--ink);
    white-space: nowrap;
  }
  .details {
    position: absolute;
    left: 197px;
    top: 410px;
    margin: 0;
    padding: 0;
    list-style: none;
    font-family: "Open Sans", sans-serif;
    color: var(--ink);
  }
  .details li { white-space: nowrap; }
  .credentials, .tagline {
    font-weight: 300;
    font-size: 28px;
    line-height: 56px;
  }
  .contact {
    font-weight: 400;
    font-size: 34px;
    line-height: 54px;
  }
  .logo {
    position: absolute;
    left: 850px;
    top: 314px;
    width: 264px;
    height: 250px;
    display: flex;
    flex-direction: column;
    align-items: center;
    justify-content: center;
    gap: 18px;
  }
  .logo-mark {
    width: 120px;
    height: 120px;
  }
  .logo-name {
    font-family: "Anton", sans-serif;
    font-size: 34px;
    letter-spacing: 1px;
    color: var(--logo-purple);
    white-space: nowrap;
  }
</style>
</head>
<body>
  <main class="card">
    <div class="side-band"></div>

    <h1 class="company-name">Build For Growth</h1>
    <p class="person-name">Dana Montreuil</p>
    <p class="person-title">Tacticraft Facililitator (R)</p>

    <ul class="details">
      <li class="credentials">RRT, B Ed (AD ed).</li>
      <li class="tagline">Engaging Transforming and Innovative</li>
      <li class="contact">tel: 416-555-0147</li>
      <li class="contact">email: danamontreuil@examplemail.com</li>
    </ul>

    <div class="logo">
      <svg class="logo-mark" viewBox="0 0 120 120" aria-hidden="true">
        <circle cx="60" cy="60" r="56" fill="var(--logo-purple)"/>
      </svg>
      <span class="logo-name">Build For Growth</span>
    </div>
  </main>
</body>
</html>
```